Need Business Card for our Real Estate Business with Sales Executive's Picture

PANTONE 484 C ( RED)

PANTONE 2766 C ( BLUE

Industry/Entity Type

Real Estate

Contact Information for Business Card

Name, Mobile, email, & picture of Person
Agency Phone, address, Web address

Requirements
Must have
• Our Logo Colours, Agent Picture,

```html
<!DOCTYPE html>
<html lang="en">
<head>
<meta charset="utf-8">
<title>Meridian – Business Card</title>
<link rel="stylesheet" href="https://fonts.googleapis.com/css2?family=Cinzel:wght@400;600&family=Tinos&display=swap">
<style>
  :root {
    --stage-light: #ececec;
    --stage-dark: #c9c9c9;
    --card-navy: #252a6c;
    --card-navy-deep: #1f2360;
    --card-glow: #3b41a0;
    --ink-white: #ffffff;
    --photo-suit: #2a3685;
    --photo-light: #4a55b0;
  }
  * { margin: 0; padding: 0; box-sizing: border-box; }
  html, body { width: 900px; height: 1200px; overflow: hidden; }
  body {
    position: relative;
    background: radial-gradient(ellipse at 50% 50%, var(--stage-light) 0%, var(--stage-dark) 100%);
    font-family: "Tinos", "Times New Roman", serif;
    color: var(--ink-white);
  }
  .card {
    position: absolute;
    left: 80px;
    width: 738px;
    height: 433px;
    border-radius: 36px;
    overflow: hidden;
    box-shadow: 0 6px 14px rgba(0,0,0,0.35);
  }
  .card--front {
    top: 130px;
    background: radial-gradient(circle at 28% 35%, var(--card-glow) 0%, var(--card-navy) 45%, var(--card-navy-deep) 100%);
  }
  .card--back {
    top: 633px;
    background: radial-gradient(ellipse at 50% 45%, var(--card-glow) 0%, var(--card-navy) 55%, var(--card-navy-deep) 100%);
  }
  .agent-photo {
    position: absolute;
    left: 16px;
    top: 15px;
    width: 246px;
    height: 418px;
    border-radius: 110px 110px 0 0;
    background: linear-gradient(180deg, var(--photo-light) 0%, var(--photo-suit) 55%, var(--card-navy-deep) 100%);
  }
  .company-name {
    position: absolute;
    font-family: "Cinzel", "Times New Roman", serif;
    font-weight: 400;
    color: var(--ink-white);
    letter-spacing: 2px;
    white-space: nowrap;
    text-align: center;
  }
  .card--front .company-name {
    left: 362px;
    width: 262px;
    top: 60px;
    font-size: 42px;
  }
  .card--back .company-name {
    left: 0;
    width: 100%;
    top: 228px;
    font-size: 52px;
  }
  .agent {
    position: absolute;
    left: 361px;
    top: 156px;
    font-family: "Cinzel", "Times New Roman", serif;
    font-weight: 600;
    line-height: 24px;
  }
  .agent-name { font-size: 21px; letter-spacing: 0.5px; }
  .agent-title { font-size: 17px; letter-spacing: 0.5px; }
  .contacts {
    position: absolute;
    left: 360px;
    top: 228px;
    list-style: none;
    font-size: 16px;
  }
  .contacts li {
    display: flex;
    align-items: center;
    height: 26px;
  }
  .contacts svg { width: 23px; height: 23px; margin-right: 6px; flex: none; }
  .address {
    position: absolute;
    left: 361px;
    top: 351px;
    font-size: 16px;
    line-height: 24px;
    font-style: normal;
  }
</style>
</head>
<body>
  <section class="card card--front">
    <div class="agent-photo" role="img" aria-label="Portrait photo of the managing director in a navy suit and striped tie"></div>
    <div class="company-name">MERIDIAN</div>
    <div class="agent">
      <div class="agent-name">DANIEL ASHFORD</div>
      <div class="agent-title">MANAGING DIRECTOR</div>
    </div>
    <ul class="contacts">
      <li>
        <svg viewBox="0 0 24 24" fill="none" stroke="currentColor" stroke-width="1.3"><circle cx="12" cy="12" r="10.5"/><rect x="9" y="6.5" width="6" height="11" rx="1"/><line x1="11" y1="15.5" x2="13" y2="15.5"/></svg>
        335-0417-5290
      </li>
      <li>
        <svg viewBox="0 0 24 24" fill="none" stroke="currentColor" stroke-width="1.3"><circle cx="12" cy="12" r="10.5"/><rect x="7" y="8.5" width="10" height="7" fill="currentColor"/><path d="M7 8.5l5 4 5-4" stroke="#252a6c"/></svg>
        danielashford@meridianrealty.au
      </li>
      <li>
        <svg viewBox="0 0 24 24" fill="none" stroke="currentColor" stroke-width="1.3"><circle cx="12" cy="12" r="10.5"/><path d="M8 7.5c-.8.8-.8 2.4.6 4.6 1.4 2.2 3.3 4 4.9 4.6 1 .4 1.9.2 2.5-.5l-1.8-1.8-1.3.9c-1-.5-2.3-1.8-2.9-2.9l.9-1.3L9.1 7.3c-.4-.2-.8 0-1.1.2z" fill="currentColor"/></svg>
        402-615-3904
      </li>
      <li>
        <svg viewBox="0 0 24 24" fill="none" stroke="currentColor" stroke-width="1.2"><circle cx="12" cy="12" r="10.5"/><circle cx="12" cy="12" r="6"/><ellipse cx="12" cy="12" rx="2.6" ry="6"/><line x1="6" y1="12" x2="18" y2="12"/></svg>
        www.meridianrealty.au
      </li>
    </ul>
    <address class="address">
      418/27 Harbourview Lane<br>
      Elmwood Bay, NSW 2577, Australia
    </address>
  </section>

  <section class="card card--back">
    <div class="company-name">MERIDIAN</div>
  </section>
</body>
</html>
```